Talent Management Company Needs Business Cards

Using one of the logos provided (attached) K&R Talent Collective needs a business card designed.
Please visit our website for more information about us-

www.krtalentcollective.example

The face should feature a dramatic presentation of the logo with the back being reserved for our professional information which is:

The information should be:
Dorian T. Vickers
C.E.O
Email: dtvickers@krtalentcollective.example
Mobile: 555-804-2917
Website: www.krtalentcollective.example

Marcus L. Vickers
Director of Public Relations
Email: mlvickers@krtalentcollective.example
Mobile: 555-806-3350

Jules R. Hampton
Director of Client Development
Email: jhampton@krtalentcollective.example

Simon Hurlock
Director of Brand Development
Email: shurlock@krtalentcollective.example

Would like the logo to have color. I would like to see one side red or black and the other side white but if it looks better in either black or red that would be fine to but would like to see how it comes out.

Please feel free to message me and if you would like just the icon alone I have other image files that I can send as well.

Target Market(s)

Professional Athletes, coaches, entertainers age 18-35 but also must be accepted in the business community

Industry/Entity Type

Business

Requirements
Must have
• 1) Use the logo
2) Double sided
3) Distinctive
Nice to have
• Small simple images for telephone, e-mail, and Url.

```html
<!DOCTYPE html>
<html lang="en">
<head>
<meta charset="utf-8">
<title>K&amp;R Talent Collective – Business Cards</title>
<link href="https://fonts.googleapis.com/css2?family=Ubuntu:wght@400;500&display=swap" rel="stylesheet">
<style>
  :root {
    --brand-red: #ed1c24;
    --brand-red-deep: #8e0b10;
    --brand-black: #000000;
    --ink: #1a1a1a;
    --ink-soft: #6d6d6d;
    --paper: #ffffff;
    --guide: #29abe2;
    --card-w: 429px;
    --card-h: 276px;
  }
  * { box-sizing: border-box; margin: 0; padding: 0; }
  html, body {
    width: 1200px; height: 874px; overflow: hidden;
    background: var(--paper);
    font-family: "Ubuntu", sans-serif;
  }
  .sheet { position: relative; width: 1200px; height: 874px; }

  .card {
    position: absolute;
    width: var(--card-w); height: var(--card-h);
    overflow: hidden;
    box-shadow: 0 3px 8px rgba(0,0,0,0.12), 0 0 2px rgba(0,0,0,0.06);
  }
  .card--front-1 { left: 130px; top: 126px; background: var(--paper); }
  .card--front-2 { left: 130px; top: 459px; background: var(--paper); }
  .card--back-black { left: 634px; top: 126px; background: var(--brand-black); }
  .card--back-red { left: 634px; top: 459px; background: var(--brand-red); }

  .ribbons { position: absolute; inset: 0; width: 100%; height: 100%; }

  .safe-guide {
    position: absolute; left: 13px; top: 13px; right: 14px; bottom: 14px;
    border: 1px solid var(--guide);
    pointer-events: none;
  }

  .brand { position: absolute; white-space: nowrap; }
  .brand__mark { display: block; width: 12px; height: 12px; background: var(--brand-red); }
  .brand__name { font-weight: 400; letter-spacing: 0.2px; line-height: 1; }

  .card--front-1 .brand, .card--front-2 .brand {
    left: 36px; top: 60px; display: flex; align-items: center; gap: 10px;
  }
  .card--front-1 .brand__name, .card--front-2 .brand__name { color: var(--ink); font-size: 19px; }

  .card--back-black .brand, .card--back-red .brand {
    left: 270px; top: 104px; transform: translateX(-50%);
    display: flex; flex-direction: column; align-items: center; gap: 40px;
  }
  .card--back-black .brand__name, .card--back-red .brand__name { color: var(--paper); font-size: 20px; }
  .card--back-red .brand__mark { background: var(--paper); }

  .person { position: absolute; left: 36px; top: 126px; }
  .person__name { font-size: 17.5px; color: var(--ink); line-height: 1.2; }
  .person__title { font-size: 13.5px; color: var(--ink-soft); line-height: 1.3; margin-top: 1px; }

  .contact { position: absolute; left: 36px; top: 184px; list-style: none; }
  .contact__item {
    display: flex; align-items: center; gap: 6px;
    font-size: 13.5px; color: var(--ink-soft); height: 19px;
  }
  .contact__item--web { color: var(--brand-red); }
  .contact__icon { width: 12px; height: 12px; flex: none; }
</style>
</head>
<body>
<main class="sheet">

  <svg width="0" height="0" style="position:absolute">
    <defs>
      <linearGradient id="grad-red" x1="0" y1="1" x2="1" y2="0">
        <stop offset="0" stop-color="#8e0b10"/><stop offset="0.55" stop-color="#ed1c24"/><stop offset="1" stop-color="#b5121a"/>
      </linearGradient>
      <linearGradient id="grad-dark" x1="0" y1="0" x2="1" y2="1">
        <stop offset="0" stop-color="#9a9a9a"/><stop offset="0.5" stop-color="#1a1a1a"/><stop offset="1" stop-color="#000"/>
      </linearGradient>
      <linearGradient id="grad-silver" x1="0" y1="0" x2="1" y2="1">
        <stop offset="0" stop-color="#ffffff"/><stop offset="1" stop-color="#9d9d9d"/>
      </linearGradient>
    </defs>
  </svg>

  <!-- Front: CEO -->
  <section class="card card--front-1">
    <svg class="ribbons" viewBox="0 0 429 276" aria-hidden="true">
      <polygon points="335,276 347,276 427,0 415,0" fill="url(#grad-dark)"/>
      <polygon points="362,276 392,276 472,0 442,0" fill="url(#grad-red)"/>
      <polygon points="404,276 418,276 498,0 484,0" fill="var(--brand-red-deep)"/>
    </svg>
    <div class="brand"><span class="brand__mark"></span><span class="brand__name">K&amp;R Talent Collective</span></div>
    <div class="person">
      <p class="person__name">Dorian T. Vickers</p>
      <p class="person__title">C.E.O</p>
    </div>
    <ul class="contact">
      <li class="contact__item">
        <svg class="contact__icon" viewBox="0 0 12 12"><circle cx="6" cy="6" r="5.3" fill="none" stroke="#444" stroke-width="1"/><path d="M4 3.2c.4-.3.8-.2 1 .2l.5 1c.1.3 0 .5-.2.7l-.3.3c.3.7.8 1.2 1.5 1.6l.3-.3c.2-.2.5-.3.7-.1l1 .5c.4.2.4.6.2 1-.5.8-1.5.9-2.5.3C4.8 7.6 3.8 6.5 3.4 5.3c-.3-.9 0-1.700.6-2.1z" fill="#444"/></svg>
        555-804-2917
      </li>
      <li class="contact__item">
        <svg class="contact__icon" viewBox="0 0 12 12"><rect x="0.8" y="2.5" width="10.4" height="7" fill="none" stroke="#444" stroke-width="1"/><path d="M0.8 2.5 6 6.6 11.2 2.5M0.8 9.5 4.6 5.5M11.2 9.5 7.4 5.5" fill="none" stroke="#444" stroke-width="1"/></svg>
        dtvickers@krtalentcollective.example
      </li>
      <li class="contact__item contact__item--web">
        <svg class="contact__icon" viewBox="0 0 12 12"><circle cx="6" cy="6" r="5" fill="#444"/><path d="M1 6h10M6 1c-2 2.8-2 7.2 0 10M6 1c2 2.8 2 7.2 0 10M2 3.5h8M2 8.5h8" fill="none" stroke="#fff" stroke-width="0.6"/></svg>
        www.krtalentcollective.example
      </li>
    </ul>
    <div class="safe-guide"></div>
  </section>

  <!-- Back: black -->
  <section class="card card--back-black">
    <svg class="ribbons" viewBox="0 0 429 276" aria-hidden="true">
      <polygon points="80,276 92,276 12,0 0,0" fill="url(#grad-silver)"/>
      <polygon points="105,276 135,276 55,0 25,0" fill="url(#grad-red)"/>
      <polygon points="145,276 157,276 77,0 65,0" fill="var(--brand-red-deep)"/>
    </svg>
    <div class="brand"><span class="brand__mark"></span><span class="brand__name">K&amp;R Talent Collective</span></div>
    <div class="safe-guide"></div>
  </section>

  <!-- Front: Director of Public Relations -->
  <section class="card card--front-2">
    <svg class="ribbons" viewBox="0 0 429 276" aria-hidden="true">
      <polygon points="335,276 347,276 427,0 415,0" fill="url(#grad-dark)"/>
      <polygon points="362,276 392,276 472,0 442,0" fill="url(#grad-red)"/>
      <polygon points="404,276 418,276 498,0 484,0" fill="var(--brand-red-deep)"/>
    </svg>
    <div class="brand"><span class="brand__mark"></span><span class="brand__name">K&amp;R Talent Collective</span></div>
    <div class="person">
      <p class="person__name">Marcus L. Vickers</p>
      <p class="person__title">Director of Public Relations</p>
    </div>
    <ul class="contact">
      <li class="contact__item">
        <svg class="contact__icon" viewBox="0 0 12 12"><circle cx="6" cy="6" r="5.3" fill="none" stroke="#444" stroke-width="1"/><path d="M4 3.2c.4-.3.8-.2 1 .2l.5 1c.1.3 0 .5-.2.7l-.3.3c.3.7.8 1.2 1.5 1.6l.3-.3c.2-.2.5-.3.7-.1l1 .5c.4.2.4.6.2 1-.5.8-1.5.9-2.5.3C4.8 7.6 3.8 6.5 3.4 5.3c-.3-.9 0-1.7.6-2.1z" fill="#444"/></svg>
        555-806-3350
      </li>
      <li class="contact__item">
        <svg class="contact__icon" viewBox="0 0 12 12"><rect x="0.8" y="2.5" width="10.4" height="7" fill="none" stroke="#444" stroke-width="1"/><path d="M0.8 2.5 6 6.6 11.2 2.5M0.8 9.5 4.6 5.5M11.2 9.5 7.4 5.5" fill="none" stroke="#444" stroke-width="1"/></svg>
        mlvickers@krtalentcollective.example
      </li>
      <li class="contact__item contact__item--web">
        <svg class="contact__icon" viewBox="0 0 12 12"><circle cx="6" cy="6" r="5" fill="#444"/><path d="M1 6h10M6 1c-2 2.8-2 7.2 0 10M6 1c2 2.8 2 7.2 0 10M2 3.5h8M2 8.5h8" fill="none" stroke="#fff" stroke-width="0.6"/></svg>
        www.krtalentcollective.example
      </li>
    </ul>
    <div class="safe-guide"></div>
  </section>

  <!-- Back: red -->
  <section class="card card--back-red">
    <svg class="ribbons" viewBox="0 0 429 276" aria-hidden="true">
      <polygon points="80,276 92,276 12,0 0,0" fill="url(#grad-dark)"/>
      <polygon points="105,276 135,276 55,0 25,0" fill="url(#grad-silver)"/>
      <polygon points="145,276 157,276 77,0 65,0" fill="#c9c9c9"/>
    </svg>
    <div class="brand"><span class="brand__mark"></span><span class="brand__name">K&amp;R Talent Collective</span></div>
    <div class="safe-guide"></div>
  </section>

</main>
</body>
</html>
```